Fennick Executive Search - New Business Card Design Project

We are an executive search firm called Fennick Executive Search based in the UK. We require a custom design for a business card. We're looking to convey a professional service to executives for executive search recruitment services. In terms of colours, we like dark blues and grays (maybe even silver incorporated somewhere if we go for a foiled type of card) but we're open to your artistic flare. See our current logo in attachments. We are totally open on design so long as the design is slick and professional.
Updates

Thanks for all your contributions of various designs. I have to say the quality of work has been amazing which is going to make our job quite difficult in the coming days on making a decision. Thanks to you all that have taken the time to submit designs thus far. We'll keep on reviewing and try to narrow down our selection as soon as possible.

Target Market(s)

Executive Search

Industry/Entity Type

Recruitment

Contact Information for Business Card

Fennick Executive Search,
Exclusively Sourcing & Hiring Senior Leaders
Gordon Pellbury, Managing Director,
07823 906417
0117 486 7132
gordon@fennickexecutive.co.uk
fennickexecutive.co.uk
58 Lindmoor Court, Hatherley Road, Bristol, BS32 9QJ

Font styles to use
Sans Serif
Other font styles liked:
• Roboto (which is used in our logo)

Requirements
Must have
• Our logo (It has a subtle fade on it from #02071d at top to #333649 at bottom)
• The logo can be on one side or both sides
• Must be elegant and professional
• We have 2nd slogan CONSULT | INSPIRE | INNOVATE | DELIVER which can be incorporated into the card
Nice to have
• Use of blues and grey colours
• Compatible with similar styling to our website fennickexecutive.co.uk
Should not have
• Must not be overly brash
• Must not contain cartoon characters

```html
<!DOCTYPE html>
<html lang="en">
<head>
<meta charset="utf-8">
<title>Fennick Executive Search – Business Card</title>
<link href="https://fonts.googleapis.com/css2?family=Roboto:wght@400;500;700&display=swap" rel="stylesheet">
<style>
  :root {
    --page-bg: #e9e9e9;
    --navy: #252a40;
    --ink: #252a40;
    --grey-text: #707070;
    --white: #ffffff;
  }
  * { margin: 0; padding: 0; box-sizing: border-box; }
  html, body {
    width: 1189px; height: 1200px; overflow: hidden;
    background: var(--page-bg);
    font-family: "Roboto", Arial, sans-serif;
  }
  .card {
    position: absolute;
    left: 222px;
    width: 757px;
    height: 490px;
    box-shadow: 0 4px 8px rgba(0,0,0,0.35);
  }
  .card--front { top: 66px; background: var(--navy); color: var(--white); }
  .card--back  { top: 625px; background: var(--white); color: var(--ink); }

  .wordmark { position: absolute; font-weight: 700; line-height: 1; white-space: nowrap; }
  .wordmark span { display: block; }

  .card--front .wordmark { left: 50%; transform: translateX(-50%); top: 173px; }
  .card--front .wordmark__name { font-size: 92px; letter-spacing: -1px; }
  .card--front .wordmark__sub  { font-size: 50px; letter-spacing: -0.5px; margin-top: -4px; }

  .front-slogan {
    position: absolute; left: 0; right: 0; top: 362px;
    text-align: center; font-size: 21px; letter-spacing: 2.3px; font-weight: 400;
  }

  .person { position: absolute; left: 40px; top: 36px; }
  .person__name  { font-size: 28px; font-weight: 700; letter-spacing: -0.3px; }
  .person__title { font-size: 22px; color: var(--grey-text); margin-top: 1px; }

  .card--back .wordmark { left: 352px; top: 36px; }
  .card--back .wordmark__name { font-size: 73px; letter-spacing: -1px; }
  .card--back .wordmark__sub  { font-size: 39px; letter-spacing: -0.5px; margin-top: 0; }

  .back-slogan {
    position: absolute; left: 353px; top: 157px;
    font-size: 18.5px; color: var(--grey-text);
  }

  .contacts { position: absolute; left: 44px; top: 377px; list-style: none; }
  .contacts li {
    display: flex; align-items: center; gap: 10px;
    font-size: 22px; color: var(--grey-text); height: 26.5px;
  }
  .contacts svg { width: 24px; height: 24px; flex: none; }

  .address {
    position: absolute; right: 38px; top: 377px;
    text-align: right; font-style: normal;
    font-size: 22px; line-height: 26.5px; color: var(--grey-text);
  }
</style>
</head>
<body>

<section class="card card--front" aria-label="Card front">
  <div class="wordmark">
    <span class="wordmark__name">FENNICK</span>
    <span class="wordmark__sub">EXECUTIVE SEARCH</span>
  </div>
  <p class="front-slogan">CONSULT | INSPIRE | INNOVATE | DELIVER</p>
</section>

<section class="card card--back" aria-label="Card back">
  <div class="person">
    <p class="person__name">Gordon Pellbury</p>
    <p class="person__title">Managing Director</p>
  </div>

  <div class="wordmark">
    <span class="wordmark__name">FENNICK</span>
    <span class="wordmark__sub">EXECUTIVE SEARCH</span>
  </div>
  <p class="back-slogan">Exclusively Sourcing &amp; Hiring Senior Leaders</p>

  <ul class="contacts">
    <li>
      <svg viewBox="0 0 22 22" aria-hidden="true">
        <circle cx="11" cy="11" r="9.5" fill="none" stroke="var(--ink)" stroke-width="2"/>
        <path d="M6 9.5c0-2 2.2-3 5-3s5 1 5 3l-1.8.6-.6-1.6H8.4l-.6 1.6z" fill="var(--ink)"/>
        <rect x="7" y="11" width="8" height="5" rx="1" fill="var(--ink)"/>
      </svg>
      07823 906417
    </li>
    <li>
      <svg viewBox="0 0 22 22" aria-hidden="true">
        <circle cx="11" cy="11" r="9.5" fill="none" stroke="var(--ink)" stroke-width="2"/>
        <rect x="8" y="5.5" width="6" height="3.5" fill="var(--ink)"/>
        <rect x="6" y="9" width="10" height="5" rx="1" fill="var(--ink)"/>
        <rect x="8" y="12.5" width="6" height="4" fill="var(--ink)" stroke="#fff" stroke-width="0.8"/>
      </svg>
      0117 486 7132
    </li>
    <li>
      <svg viewBox="0 0 22 22" aria-hidden="true">
        <circle cx="11" cy="11" r="9.5" fill="none" stroke="var(--ink)" stroke-width="2"/>
        <rect x="6" y="7.5" width="10" height="7" fill="var(--ink)"/>
        <path d="M6.3 7.8 11 11.5l4.7-3.7" fill="none" stroke="#fff" stroke-width="1"/>
      </svg>
      gordon@fennickexecutive.co.uk
    </li>
  </ul>

  <address class="address">
    58 Lindmoor Court<br>
    Hatherley Road<br>
    Bristol, BS32 9QJ
  </address>
</section>

</body>
</html>
```